PowerPoint Template Design

We are an independent private equity and advisory firm (mergers and acquisitions), based in Brazil. We are looking for a power point template to use for companies presentations to investors and other targets (ie competitors).
Find attached the actual template that we use, we need something with this structure but more customized.

- Cover slide with our logo, project name and current date
- Index/Agenda slide
- Content slides
a. Slide with title, subtitle, text and footer. The footer should contain the page number, the person who we are sending to and the word "CONFIDENTIAL"
b. Slide with title, subtitle, text and pictures/charters/graphics
- Final slide with adress and contacts

We do not want something very colorful, we need something plain, simple but modern.

Target Market(s)

Investors, CEOs, CFOs, other advisory firms like DNTallis, DSRH, Almsbury, etc.

Industry/Entity Type

Equity

Requirements
Must have
• - the same colors used by our designer;
- one font only (Century Gothic);

```html
<!DOCTYPE html>
<html lang="en">
<head>
<meta charset="utf-8">
<title>Cover Slide – Project Name</title>
<link rel="stylesheet" href="https://fonts.googleapis.com/css2?family=Poppins:wght@400;600&display=swap">
<style>
  :root {
    --band-dark: #3d3e40;
    --band-stripe: #333436;
    --band-darker: #2a2b2d;
    --band-black: #1b1b1c;
    --accent-yellow: #f6ae1a;
    --accent-yellow-deep: #d98f0b;
    --stage-light: #f2f1ee;
    --stage-mid: #d6d5d1;
    --stage-edge: #c4c3bf;
    --title-grey: #505354;
    --brand-ink: #3a3b3d;
    --paper: #ffffff;
  }

  * { margin: 0; padding: 0; box-sizing: border-box; }

  html, body {
    width: 1200px;
    height: 900px;
    overflow: hidden;
    background: var(--paper);
  }

  .slide {
    position: relative;
    width: 1200px;
    height: 900px;
    overflow: hidden;
    font-family: "Poppins", "Century Gothic", sans-serif;
    background: radial-gradient(ellipse 640px 520px at 600px 420px,
                var(--stage-light) 0%, var(--stage-mid) 70%, var(--stage-edge) 100%);
  }

  /* Top header bands */
  .header-band {
    position: absolute;
    left: 0; top: 0;
    width: 100%;
    height: 64px;
    background:
      repeating-linear-gradient(to right, var(--band-stripe) 0 2px, var(--band-dark) 2px 5px);
  }
  .header-accent {
    position: absolute;
    left: 0; top: 64px;
    width: 100%;
    height: 22px;
    background: linear-gradient(to bottom, var(--accent-yellow) 0%, var(--accent-yellow-deep) 100%);
  }
  .header-rule {
    position: absolute;
    left: 0; top: 86px;
    width: 100%;
    height: 16px;
    background: linear-gradient(to bottom, var(--band-darker) 0%, #555658 100%);
    box-shadow: 0 3px 5px rgba(0,0,0,0.25);
  }

  /* Brand box */
  .brand-box {
    position: absolute;
    left: 914px; top: 0;
    width: 234px;
    height: 224px;
    background: var(--paper);
    box-shadow: 2px 4px 8px rgba(0,0,0,0.35);
    display: flex;
    align-items: center;
    justify-content: center;
    padding-top: 30px;
  }
  .brand-name {
    font-weight: 600;
    font-size: 28px;
    line-height: 1;
    color: var(--brand-ink);
  }

  /* Title */
  .project-title {
    position: absolute;
    left: 0; top: 440px;
    width: 100%;
    text-align: center;
    font-weight: 600;
    font-size: 78px;
    line-height: 1;
    letter-spacing: 0;
    color: var(--title-grey);
  }

  /* Footer bands */
  .footer-band {
    position: absolute;
    left: 0; top: 823px;
    width: 100%;
    height: 40px;
    background: var(--band-black);
    display: flex;
    align-items: center;
    justify-content: flex-end;
    padding-right: 20px;
  }
  .slide-date {
    font-size: 17px;
    font-weight: 400;
    color: var(--paper);
  }
  .footer-accent {
    position: absolute;
    left: 0; top: 863px;
    width: 100%;
    height: 22px;
    background: linear-gradient(to bottom, var(--accent-yellow) 0%, var(--accent-yellow-deep) 100%);
  }
  .footer-base {
    position: absolute;
    left: 0; top: 885px;
    width: 100%;
    height: 15px;
    background: linear-gradient(to bottom, #4a4b4d 0%, #6a6b6d 100%);
  }
</style>
</head>
<body>
  <main class="slide">
    <div class="header-band"></div>
    <div class="header-accent"></div>
    <div class="header-rule"></div>

    <div class="brand-box">
      <span class="brand-name">Alvora Capital</span>
    </div>

    <h1 class="project-title">project name</h1>

    <footer class="footer-band">
      <time class="slide-date" datetime="2013-05-16">5/16/ 2013</time>
    </footer>
    <div class="footer-accent"></div>
    <div class="footer-base"></div>
  </main>
</body>
</html>
```